Quorra Desk Relay Chat Monitor Interface

We have a live help chat software that we need a new chat monitor interface designed for. Something that will be easy to make responsive. I will provide screen shots of the current interface and a picture of the new admin back-end that we want it to look similar too. This project should be fairly straight forward and easy. See below.

Important Notes:

1. You DO NOT need to worry about the actual list of visitors on the site in the middle as that will be handled by the grid system we use.

2. We have decided to eliminate the logo from the monitor all together to make it more compact. Just the words "Quorra Desk Relay" and a copyright notice will be enough.

3. We want the chat monitor interface to utilize the same colors and look as the new admin interface if possible. See attached "new_admin_interface.png" image.

4. Although I want to utilize the same colors as the admin area, it should NOT utilize the same header and footer as the admin area. I only referenced the admin area so that you can get color ideas from it. Consider it a popup window and assume the same amount of space will be used. Although it will have the ability to be resized we must not waste space.

Target Market(s)

N/A

Industry/Entity Type

Software

Number of Pages Required

1 page

Requirements
Must have
• See Description.
Nice to have
• See Description.
Should not have
• See Description.

```html
<!DOCTYPE html>
<html lang="en">
<head>
<meta charset="utf-8">
<title>Quorra Desk Relay – Chat Monitor</title>
<link href="https://fonts.googleapis.com/css2?family=Montserrat:wght@400;500;600&display=swap" rel="stylesheet">
<style>
:root{
  --header-top:#4a5b6c;
  --header-bottom:#2c3a48;
  --nav-bg:#263341;
  --nav-text:#ffffff;
  --table-head-top:#5fa55a;
  --table-head-bottom:#3d7f2f;
  --row-dark:#2a3a4c;
  --row-light:#3f5064;
  --row-text:#e9eef3;
  --cell-border:#51606f;
  --panel-bg:#ffffff;
  --panel-head:#f1f1f1;
  --panel-border:#e2e2e2;
  --body-text:#333c45;
  --link-green:#3d8f3a;
  --footer-bg:#2b3947;
}
*{box-sizing:border-box;margin:0;padding:0}
html,body{width:1200px;height:1039px;overflow:hidden}
body{font-family:"Montserrat",sans-serif;color:var(--body-text);
  background:radial-gradient(ellipse at 60% 40%,#eef4f6 0%,#dde7ec 55%,#cfd9e0 100%);position:relative}
.app-header{position:absolute;left:0;top:0;width:1200px;height:80px;
  background:linear-gradient(var(--header-top),var(--header-bottom));color:#fff}
.brand{position:absolute;left:132px;top:29px;font-size:22px;font-weight:500;letter-spacing:.2px}
.copyright-top{position:absolute;right:132px;top:19px;font-size:11.5px;color:#dbe2e8}
.menu-links{position:absolute;left:660px;top:48px;font-size:12px;display:flex;gap:24px;color:#dfe5ea}
.menu-links span+span{border-left:1px solid #5b6a78;padding-left:24px}
.status-box{position:absolute;left:850px;top:42px;display:flex;align-items:center;gap:8px;font-size:12px}
.select{display:flex;align-items:center;justify-content:space-between;height:27px;padding:0 10px;
  border:1px solid #5e6e7d;background:#2f3d4b;color:#fff;font-size:12px}
.status-box .select{width:176px}
.dot{width:13px;height:13px;border-radius:50%;background:radial-gradient(circle at 35% 30%,#b8f5a8,#35b02c 55%,#1d6e19);display:inline-block}
.main-nav{position:absolute;left:0;top:80px;width:1200px;height:49px;background:var(--nav-bg);
  border-top:1px solid #3b4a59;display:flex;align-items:center;padding-left:132px;font-size:12px;color:var(--nav-text);font-weight:500}
.nav-home{width:42px;height:29px;background:#1b2733;display:flex;align-items:center;justify-content:center;margin-right:23px}
.nav-item{display:flex;align-items:center;gap:8px;margin-right:37px}
.nav-item svg{flex:none}
.visitor-table{position:absolute;left:132px;top:184px;width:936px;border-collapse:collapse;table-layout:fixed;font-size:9.5px;color:var(--row-text)}
.visitor-table th{height:51px;background:linear-gradient(var(--table-head-top),var(--table-head-bottom));
  color:#fff;font-size:12px;font-weight:500;text-align:left;padding-left:15px;border-right:1px solid #4b8e42;white-space:nowrap;overflow:hidden}
.visitor-table th:last-child{border-right:0}
.visitor-table td{height:49px;border-right:1px solid var(--cell-border);padding-left:8px;white-space:nowrap;overflow:hidden;text-overflow:ellipsis}
.visitor-table td:last-child{border-right:0}
.visitor-table tr:nth-child(odd) td{background:var(--row-dark)}
.visitor-table tr:nth-child(even) td{background:var(--row-light)}
.visitor-table tr:first-child td{height:48px}
.cell-center{text-align:center;padding-left:0!important}
.ip{display:flex;align-items:center;gap:2px}
.browser-mark{display:inline-block;width:20px;height:20px;border-radius:50%;background:#d9d9d9;border:5px solid #4a8fe0;vertical-align:middle}
.os-mark{display:inline-block;width:20px;height:18px;background:#e0a23a;vertical-align:middle}
.detail-panel{position:absolute;left:132px;top:535px;width:720px;height:410px;background:var(--panel-bg);border:1px solid var(--panel-border)}
.tab-bar{height:48px;background:var(--panel-head);display:flex;align-items:flex-end;padding-left:14px;position:relative}
.tab{display:flex;align-items:center;gap:6px;height:37px;padding:0 7px;font-size:12.5px;font-weight:500;color:#2c3540;margin-right:10px}
.tab.active{background:#fff}
.tab-bar .select{position:absolute;left:517px;top:12px;width:182px;height:26px;background:#fff;color:#333;border-color:#d5d5d5;font-size:11.5px}
.info-list{position:absolute;left:28px;top:90px;font-size:11.5px}
.info-row{display:flex;height:28px;align-items:flex-start;white-space:nowrap}
.info-row dt{width:86px}
.info-row dd{margin-left:0}
.info-row a{color:var(--link-green)}
.flag{display:inline-block;width:19px;height:12px;background:#3b4d8c;vertical-align:-1px;margin-right:3px}
.operators-panel{position:absolute;left:885px;top:535px;width:183px;height:410px;background:var(--panel-bg);border:1px solid var(--panel-border)}
.operators-panel h2{height:48px;background:var(--panel-head);font-size:12px;font-weight:500;padding:16px 0 0 16px}
.operator{display:flex;align-items:center;gap:5px;font-size:11.5px;padding:8px 0 0 13px}
.operator .dot{width:16px;height:16px}
.app-footer{position:absolute;left:0;top:977px;width:1200px;height:62px;background:var(--footer-bg);
  color:#fff;font-size:13px;text-align:center;line-height:62px}
</style>
</head>
<body>
<header class="app-header">
  <div class="brand">Quorra Desk Relay</div>
  <div class="copyright-top">Quorra Desk Relay © 2016</div>
  <nav class="menu-links"><span>File</span><span>Actions</span></nav>
  <div class="status-box">Status:
    <div class="select"><span style="display:flex;align-items:center;gap:12px"><span class="dot"></span>Online</span>
      <svg width="8" height="12" viewBox="0 0 8 12"><path d="M1 5l3-3 3 3M1 7l3 3 3-3" stroke="#fff" fill="none" stroke-width="1.5"/></svg></div>
  </div>
</header>

<nav class="main-nav">
  <div class="nav-home"><svg width="14" height="12" viewBox="0 0 14 12"><path d="M7 0L0 6h2v6h4V8h2v4h4V6h2z" fill="#fff"/></svg></div>
  <div class="nav-item"><svg width="10" height="11" viewBox="0 0 10 11"><circle cx="5" cy="3" r="2.8" fill="#fff"/><path d="M0 11c0-4 10-4 10 0z" fill="#fff"/></svg>Operators<svg width="8" height="5" viewBox="0 0 8 5"><path d="M1 1l3 3 3-3" stroke="#fff" fill="none"/></svg></div>
  <div class="nav-item"><svg width="11" height="11" viewBox="0 0 11 11"><rect x="1" y="4" width="9" height="7" fill="#fff"/><rect x="0" y="2" width="11" height="3" fill="#fff"/><rect x="5" y="2" width="1" height="9" fill="#263341"/></svg>Departments<svg width="8" height="5" viewBox="0 0 8 5"><path d="M1 1l3 3 3-3" stroke="#fff" fill="none"/></svg></div>
  <div class="nav-item"><svg width="13" height="10" viewBox="0 0 13 10"><path d="M.5 1h4l1 1.5h5v7H.5z M.5 9.5L3 4h9.5L10.5 9.5" stroke="#fff" fill="none"/></svg>Transcripts<svg width="8" height="5" viewBox="0 0 8 5"><path d="M1 1l3 3 3-3" stroke="#fff" fill="none"/></svg></div>
  <div class="nav-item"><svg width="11" height="11" viewBox="0 0 11 11"><circle cx="5.5" cy="5.5" r="3.5" stroke="#fff" stroke-width="3" fill="none" stroke-dasharray="2 1.2"/><circle cx="5.5" cy="5.5" r="1.2" fill="#fff"/></svg>Settings<svg width="8" height="5" viewBox="0 0 8 5"><path d="M1 1l3 3 3-3" stroke="#fff" fill="none"/></svg></div>
  <div class="nav-item"><svg width="9" height="11" viewBox="0 0 9 11"><path d="M0 0h6l3 3v8H0z" fill="#fff"/><path d="M2 5h5M2 7h5M2 9h5" stroke="#263341"/></svg>Reports<svg width="8" height="5" viewBox="0 0 8 5"><path d="M1 1l3 3 3-3" stroke="#fff" fill="none"/></svg></div>
  <div class="nav-item"><svg width="11" height="10" viewBox="0 0 11 10"><rect x="0" y="0" width="11" height="3" fill="#fff"/><rect x="1" y="4" width="9" height="6" fill="#fff"/><rect x="4" y="5" width="3" height="1" fill="#263341"/></svg>Actions<svg width="8" height="5" viewBox="0 0 8 5"><path d="M1 1l3 3 3-3" stroke="#fff" fill="none"/></svg></div>
</nav>

<table class="visitor-table">
  <colgroup><col style="width:92px"><col style="width:120px"><col style="width:74px"><col style="width:57px"><col style="width:469px"><col style="width:73px"><col style="width:51px"></colgroup>
  <thead><tr><th>IP Address</th><th style="padding-left:18px">Status</th><th style="padding-left:9px">Duration</th><th style="padding-left:14px">Pages</th><th style="padding-left:12px">Location</th><th style="padding-left:13px">Browser</th><th style="padding-left:15px">OS</th></tr></thead>
  <tbody>
    <tr><td style="padding-left:6px"><span class="ip"><svg width="12" height="12" viewBox="0 0 12 12"><circle cx="6" cy="3.5" r="3" fill="#5fae4f"/><path d="M0 12c0-5 12-5 12 0z" fill="#5fae4f"/></svg>71.104.58.59</span></td><td style="padding-left:19px">Chatting "mvarden"</td><td style="padding-left:19px">0:40:01</td><td class="cell-center">17</td><td style="padding-left:14px">https://www.brellwick-hosting.net/billing/admin/supporttickets.php?filter=1</td><td class="cell-center"><span class="browser-mark"></span></td><td class="cell-center"><span class="os-mark"></span></td></tr>
    <tr><td style="padding-left:6px"><span class="ip"><svg width="12" height="12" viewBox="0 0 12 12"><circle cx="6" cy="3.5" r="3" fill="#5fae4f"/><path d="M0 12c0-5 12-5 12 0z" fill="#5fae4f"/></svg>75.142.132.122</span></td><td style="padding-left:19px">In Site</td><td style="padding-left:20px">0:17:02</td><td class="cell-center">1</td><td style="padding-left:14px">http://forum.kestrin-labs.net/showthread.php?7516-Help!!!-General-settings-page-in-Admin-mode-..</td><td class="cell-center"><span class="browser-mark"></span></td><td class="cell-center"><span class="os-mark"></span></td></tr>
    <tr><td style="padding-left:6px"><span class="ip"><svg width="12" height="12" viewBox="0 0 12 12"><circle cx="6" cy="3.5" r="3" fill="#5fae4f"/><path d="M0 12c0-5 12-5 12 0z" fill="#5fae4f"/></svg>199.201.102.196</span></td><td style="padding-left:20px">In Site</td><td style="padding-left:21px">0:26:14</td><td class="cell-center">1</td><td style="padding-left:14px">https://www.brellwicktools.net/shopping-cart-software.html</td><td class="cell-center"><span class="browser-mark"></span></td><td class="cell-center"><span class="os-mark"></span></td></tr>
    <tr><td style="padding-left:6px"><span class="ip"><svg width="12" height="12" viewBox="0 0 12 12"><circle cx="6" cy="3.5" r="3" fill="#5fae4f"/><path d="M0 12c0-5 12-5 12 0z" fill="#5fae4f"/></svg>66.42.219.226</span></td><td style="padding-left:19px">In Site</td><td style="padding-left:23px">0:26:06</td><td class="cell-center">8</td><td style="padding-left:14px">http://my.kestrin-labs.net/announcements.php?page=2</td><td class="cell-center"><span class="browser-mark"></span></td><td class="cell-center"><span class="os-mark"></span></td></tr>
  </tbody>
</table>

<section class="detail-panel">
  <div class="tab-bar">
    <div class="tab active"><svg width="18" height="18" viewBox="0 0 18 18"><circle cx="9" cy="9" r="8" stroke="#4c9a3c" stroke-width="1.6" fill="none"/><circle cx="9" cy="5" r="1.2" fill="#4c9a3c"/><rect x="8" y="7.5" width="2" height="6" fill="#4c9a3c"/></svg>Visitors Info</div>
    <div class="tab"><svg width="19" height="16" viewBox="0 0 19 16"><ellipse cx="9.5" cy="11" rx="5" ry="4.5" fill="#4c9a3c"/><circle cx="3" cy="6" r="2.2" fill="#4c9a3c"/><circle cx="7" cy="2.5" r="2.2" fill="#4c9a3c"/><circle cx="12" cy="2.5" r="2.2" fill="#4c9a3c"/><circle cx="16" cy="6" r="2.2" fill="#4c9a3c"/></svg>Footprints</div>
    <div class="tab"><svg width="18" height="17" viewBox="0 0 18 17"><path d="M9 1C4.6 1 1 3.9 1 7.5c0 2 1 3.7 2.7 4.9L3 16l4-2.3c.6.1 1.3.2 2 .2 4.4 0 8-2.9 8-6.5S13.4 1 9 1z" fill="#4c9a3c"/><circle cx="6" cy="7.5" r="1" fill="#fff"/><circle cx="9" cy="7.5" r="1" fill="#fff"/><circle cx="12" cy="7.5" r="1" fill="#fff"/></svg>Chats</div>
    <div class="select">Transfer to:<svg width="8" height="11" viewBox="0 0 8 11"><path d="M0 4l4-4 4 4zM0 7l4 4 4-4z" fill="#333"/></svg></div>
  </div>
  <dl class="info-list">
    <div class="info-row"><dt>IP Address</dt><dd>: &nbsp;<span class="flag"></span><a href="#">199.201.102.196</a></dd></div>
    <div class="info-row"><dt>Hostname</dt><dd>: &nbsp;199-201-102-196.ut.ostavelnet.example</dd></div>
    <div class="info-row"><dt>Referer</dt><dd>: &nbsp;&nbsp;<a href="#">https://www.searchwell.example/</a></dd></div>
    <div class="info-row"><dt>User Agent</dt><dd>: &nbsp;&nbsp;Netvia/5.0 (Panesys NT 6.1;WXE64) LayoutKit/537.36 (RNDR, like Tessel) Strata/52.0.2743.116 Rover/53...</dd></div>
    <div class="info-row"><dt>Brow &amp; OS</dt><dd>: &nbsp;&nbsp;Strata 52.0.2743.116 - Panesys 7</dd></div>
    <div class="info-row"><dt>Screen Res</dt><dd>: &nbsp;&nbsp;1920 * 1080</dd></div>
    <div class="info-row"><dt>Local Time</dt><dd>: &nbsp;&nbsp;4:30:30 PM</dd></div>
    <div class="info-row"><dt>Time Online</dt><dd>: &nbsp;&nbsp;0:24:09</dd></div>
    <div class="info-row"><dt>Transcripts</dt><dd>: &nbsp;&nbsp;<a href="#">0</a></dd></div>
  </dl>
</section>

<aside class="operators-panel">
  <h2>Operators</h2>
  <div class="operator"><span class="dot"></span>Dana R.</div>
</aside>

<footer class="app-footer">© 2016 QUORRA DESK RELAY. All rights Reserved.</footer>
</body>
</html>
```